Maple Rx Ventures (company name is Maple Rx Ventures LLP)

management of homestay, hospitality something similar with https://www.stayvorn.example

Target Market(s)

johor bahru market (Malaysia)

Contact Information for Business Card

Maple Ventures Rx LLP

Logo Text

eyes catching, attractive, amazing, Nice, jaw dropping for design

Coding

Coded - Design and coding required

Number of Pages Required

5+ page

Colors

Designer to choose colors to be used in the design.

Requirements
Must have
• please change the short term proposal to our company logo and change the name from stayvorn to maple RX Ventures LLP
• thanks
Nice to have
• please let me have eyes catching , jaw dropping design

```html
<!DOCTYPE html>
<html lang="en">
<head>
<meta charset="utf-8">
<title>Maple Rx Ventures</title>
<link href="https://fonts.googleapis.com/css2?family=Raleway:wght@400;500;600;700&family=Allura&display=swap" rel="stylesheet">
<style>
:root{
  --purple:#4b1f72;
  --purple-deep:#2e1046;
  --ink:#222;
  --muted:#666;
  --script:#c9c9c9;
  --panel:#efeff1;
  --footer:#1b1b1b;
  --footer-deep:#111;
  --white:#fff;
}
*{box-sizing:border-box;margin:0;padding:0}
html,body{width:1200px;height:3125px;overflow:hidden}
body{position:relative;background:var(--white);font-family:'Raleway',sans-serif;color:var(--ink)}
.abs{position:absolute}
.topbar{left:0;top:0;width:1200px;height:33px;background:var(--purple-deep);color:#ddd;font-size:11px;display:flex;align-items:center;padding:0 0 0 130px;gap:20px}
.topbar span{display:flex;align-items:center;gap:8px}
.topbar .social{position:absolute;right:130px;top:11px;display:flex;gap:8px}
.topbar .social i{display:block;width:11px;height:11px;border-radius:50%;background:#ddd}
.hero-photo{left:0;top:33px;width:1200px;height:671px;background:linear-gradient(160deg,#5b5655 0%,#3d3a3a 40%,#6f6b68 70%,#2f2c2c 100%)}
.hero-shade{left:0;top:33px;width:1200px;height:671px;background:rgba(0,0,0,.25)}
.header{left:0;top:33px;width:1200px;height:100px;background:rgba(245,245,245,.93);display:flex;align-items:center;padding:0 130px}
.brand{font-weight:700;font-size:23px;letter-spacing:1px;color:var(--ink)}
.nav{margin-left:auto;display:flex;gap:32px;font-size:15px;color:#333}
.hero-title{left:0;width:1200px;top:330px;text-align:center;color:var(--white);font-weight:500;font-size:58px}
.hero-text{left:220px;width:760px;top:432px;text-align:center;color:#eee;font-size:14px;line-height:1.4}
.btn-outline{left:479px;top:496px;width:244px;height:52px;border:1.5px solid #eee;color:var(--white);font-size:22px;letter-spacing:1.5px;display:flex;align-items:center;justify-content:center}
.script{font-family:'Allura',cursive;color:var(--script);font-size:50px;line-height:1}
.sec-title{font-size:24px;color:var(--ink);letter-spacing:.5px}
.center{left:0;width:1200px;text-align:center}
.lead{color:var(--muted);font-size:12.5px;line-height:1.35;text-align:center}
.story-card{top:948px;width:262px;height:185px;box-shadow:0 6px 14px rgba(0,0,0,.3);overflow:hidden}
.story-card .fill{position:absolute;inset:0}
.story-card .tint{position:absolute;inset:0;background:rgba(0,0,0,.35)}
.story-card .label{position:absolute;left:0;right:0;top:112px;text-align:center;color:var(--white);font-size:19px;line-height:1.2}
.story-card svg{position:absolute;left:107px;top:30px}
.dots{display:flex;gap:6px;justify-content:center}
.dots i{width:7px;height:7px;border-radius:50%;background:var(--purple)}
.services-photo{left:0;top:1246px;width:600px;height:475px;background:linear-gradient(135deg,#b7a58e 0%,#6a5948 45%,#2f2a26 70%,#c6bcae 100%)}
.services-panel{left:600px;top:1246px;width:600px;height:475px;background:var(--panel)}
.services-copy{left:646px;width:450px;font-size:13px;line-height:1.35;color:#555}
.btn-solid{background:var(--purple);color:var(--white);display:flex;align-items:center;justify-content:center;font-size:18px;letter-spacing:1px}
.why-card{top:1960px;width:223px;height:196px;border:1.5px solid #ccc;border-radius:8px;background:var(--white);text-align:center;color:#333;font-size:19px}
.why-card svg{display:block;margin:34px auto 14px}
.why-card.active{background:linear-gradient(160deg,#3d3533,#1d1a19);border-color:#1d1a19;color:var(--white)}
.why-card.active h3{font-weight:400;font-size:19px;margin-top:50px;line-height:1.2}
.why-card.active p{font-size:12.5px;line-height:1.25;margin-top:10px;padding:0 18px}
.offer-photo{left:0;top:2258px;width:1200px;height:390px;background:linear-gradient(180deg,#2b2723 0%,#4a3b2c 40%,#1f2c33 75%,#12181c 100%)}
.offer-shade{left:0;top:2258px;width:1200px;height:390px;background:rgba(0,0,0,.45)}
.offer-title{font-size:24px;color:var(--white)}
.email{left:421px;top:2469px;width:358px;height:35px;background:rgba(255,255,255,.35);color:#eee;font-size:10px;padding:12px 0 0 26px}
.agree{left:421px;top:2516px;color:#eee;font-size:10px;display:flex;align-items:center;gap:16px}
.agree i{display:block;width:12px;height:12px;background:var(--white)}
.partners{left:0;top:2648px;width:1200px;height:200px;background:var(--white)}
.badge{top:2728px;height:44px;border-radius:6px}
.footer{left:0;top:2848px;width:1200px;height:256px;background:var(--footer)}
.footer-base{left:0;top:3104px;width:1200px;height:21px;background:var(--footer-deep);color:#ccc;font-size:9px;text-align:center;line-height:21px}
.f-head{top:2884px;color:var(--white);font-size:20px;letter-spacing:.5px}
.f-text{color:#ddd;font-size:12.5px;line-height:1.3}
.f-links{color:#ddd;font-size:13px;line-height:30px}
.contact-row{display:flex;gap:18px;align-items:flex-start}
</style>
</head>
<body>

<div class="abs topbar">
  <span><svg width="11" height="11" viewBox="0 0 24 24"><path fill="#ddd" d="M6.6 10.8a15 15 0 0 0 6.6 6.6l2.2-2.2a1 1 0 0 1 1-.25 11 11 0 0 0 3.6.6 1 1 0 0 1 1 1V20a1 1 0 0 1-1 1A17 17 0 0 1 3 4a1 1 0 0 1 1-1h3.5a1 1 0 0 1 1 1 11 11 0 0 0 .6 3.6 1 1 0 0 1-.25 1z"/></svg>+65 8123 4567</span>
  <span><svg width="11" height="13" viewBox="0 0 24 28"><path fill="#ddd" d="M12 0a9 9 0 0 0-9 9c0 7 9 19 9 19s9-12 9-19a9 9 0 0 0-9-9zm0 13a4 4 0 1 1 0-8 4 4 0 0 1 0 8z"/></svg>L12-07 Cedar Court, Jalan Seroja, Taman Bayu, 81200 Johor Bahru.</span>
  <div class="social"><i></i><i></i><i></i><i></i></div>
</div>

<div class="abs hero-photo" role="img" aria-label="Photo of a modern bedroom with a grey upholstered bed, pillows and framed art"></div>
<div class="abs hero-shade"></div>
<header class="abs header">
  <div class="brand">MAPLE RX VENTURES</div>
  <nav class="nav"><span>Explore The Place</span><span>Shop The Place</span><span>Blog</span><span>Our Story</span><span>Let's Talk</span></nav>
</header>
<h1 class="abs hero-title">Maximize Your Rental Income</h1>
<p class="abs hero-text">Lorem ipsum dolor sit amet, dolor aliquam vehicula, eget vehicula condimentum ante arcu, sed amet imperdiet urna, dictum phasellus dolor. Parturient vel sed felis montes dui, rutrum nullam auctor orci ea id, sed amet massa nibh.</p>
<div class="abs btn-outline">BOOK NOW</div>

<div class="abs center script" style="top:762px">welcome to</div>
<h2 class="abs center sec-title" style="top:797px">OUR STORY</h2>
<p class="abs lead" style="left:330px;width:540px;top:858px">Lorem ipsum dolor sit amet, dolor aliquam vehicula, eget vehicula condimentum ante arcu, sed amet imperdiet urna, dictum phasellus dolor. Parturient vel sed felis montes dui, rutrum nullam auctor orci ea id, sed amet massa nibh</p>

<div class="abs story-card" style="left:177px">
  <div class="fill" role="img" aria-label="Photo of a key being handed over at check-in" style="background:linear-gradient(135deg,#8c8a86,#4b4845 60%,#2a2826)"></div>
  <div class="tint"></div>
  <svg width="48" height="56" viewBox="0 0 48 56"><path d="M24 4a14 14 0 0 0-14 14c0 11 14 26 14 26s14-15 14-26A14 14 0 0 0 24 4z" fill="none" stroke="#fff" stroke-width="3"/><circle cx="24" cy="18" r="5" fill="none" stroke="#fff" stroke-width="3"/></svg>
  <div class="label">Check Ins / Outs</div>
</div>
<div class="abs story-card" style="left:473px">
  <div class="fill" role="img" aria-label="Photo of a laundry room with a washing machine and cleaning supplies" style="background:linear-gradient(135deg,#8a6a4d,#5a4a3c 55%,#3a3430)"></div>
  <div class="tint"></div>
  <svg width="48" height="56" viewBox="0 0 48 56"><path d="M24 6C24 6 10 24 10 34a14 14 0 0 0 28 0C38 24 24 6 24 6z" fill="none" stroke="#fff" stroke-width="3"/><path d="M40 6v8M36 10h8" stroke="#fff" stroke-width="2"/></svg>
  <div class="label">Cleaning Laundry &amp;<br>Maintenance</div>
</div>
<div class="abs story-card" style="left:765px">
  <div class="fill" role="img" aria-label="Photo of a desk with a keyboard and marketing papers" style="background:linear-gradient(135deg,#9a9a9a,#5c5c5c 55%,#8a2a2a)"></div>
  <div class="tint"></div>
  <svg width="52" height="56" viewBox="0 0 52 56"><path d="M8 22h8l20-12v34L16 32H8z" fill="none" stroke="#fff" stroke-width="3" stroke-linejoin="round"/><path d="M14 32l4 14h6l-3-13" fill="none" stroke="#fff" stroke-width="3"/><path d="M42 20l6-4M42 27h7M42 34l6 4" stroke="#fff" stroke-width="2.5"/></svg>
  <div class="label">Marketing &amp;<br>Optimization</div>
</div>
<div class="abs dots" style="left:0;width:1200px;top:1182px"><i></i><i></i><i></i><i></i></div>

<div class="abs services-photo" role="img" aria-label="Photo of a living room with sofas, a TV wall and a chandelier"></div>
<div class="abs services-panel"></div>
<div class="abs script" style="left:646px;top:1296px">professional</div>
<h2 class="abs sec-title" style="left:646px;top:1338px">OUR SERVICES</h2>
<p class="abs services-copy" style="top:1396px">We provide 24/7 customer support and assistance to ensure you have a great experience during your stay.We strive to be industrious to offer you the best value and service at the top of our priority during your Staycation, Holiday and Business Trip.</p>
<p class="abs services-copy" style="top:1474px">We also ensure to provide you with a clean environment by the professional housekeeping team. A remarkable guesthouse experience you should deserve during your stay!</p>
<div class="abs btn-solid" style="left:646px;top:1554px;width:173px;height:48px">READ MORE</div>

<div class="abs center script" style="top:1771px">stay updated</div>
<h2 class="abs center sec-title" style="top:1812px">WHY SHORT STAY RENTAL?</h2>
<p class="abs lead" style="left:330px;width:540px;top:1879px">Lorem ipsum dolor sit amet, dolor aliquam vehicula, eget vehicula condimentum ante arcu, sed amet imperdiet urna, dictum phasellus dolor. Parturient vel sed felis montes dui, rutrum nullam auctor orci ea id, sed amet massa nibh</p>

<div class="abs why-card active" style="left:135px" role="img" aria-label="Dark photo of a room behind the card text">
  <h3>Higher Rental<br>Income Potential</h3>
  <p>We distribute accross popular OTA, Roomnest, Staylist etc to maximize your income.</p>
</div>
<div class="abs why-card" style="left:373px">
  <svg width="52" height="50" viewBox="0 0 52 50"><path d="M4 24L26 6l22 18" fill="none" stroke="#4b1f72" stroke-width="3"/><path d="M10 20v26h32V20" fill="none" stroke="#4b1f72" stroke-width="3"/><rect x="16" y="26" width="8" height="8" fill="none" stroke="#4b1f72" stroke-width="2"/><rect x="28" y="26" width="8" height="8" fill="none" stroke="#4b1f72" stroke-width="2"/><rect x="22" y="36" width="8" height="10" fill="none" stroke="#4b1f72" stroke-width="2"/></svg>
  Well Maintain<br>House Condition
</div>
<div class="abs why-card" style="left:608px">
  <svg width="52" height="52" viewBox="0 0 52 52"><circle cx="26" cy="26" r="23" fill="none" stroke="#4b1f72" stroke-width="3"/><circle cx="26" cy="26" r="15" fill="none" stroke="#4b1f72" stroke-width="2"/><path d="M18 31l6-6 4 4 7-8" fill="none" stroke="#4b1f72" stroke-width="2.5"/></svg>
  New Trends
</div>
<div class="abs why-card" style="left:844px">
  <svg width="52" height="52" viewBox="0 0 52 52"><circle cx="28" cy="20" r="15" fill="none" stroke="#4b1f72" stroke-width="3"/><circle cx="28" cy="20" r="8" fill="none" stroke="#4b1f72" stroke-width="2"/><path d="M18 32L6 46M10 38l-4 2M14 42l-2 4" stroke="#4b1f72" stroke-width="3" fill="none"/></svg>
  High Demands
</div>
<div class="abs dots" style="left:0;width:1200px;top:2203px"><i></i><i></i><i></i><i></i></div>

<div class="abs offer-photo" role="img" aria-label="Night photo of a villa courtyard with a swimming pool"></div>
<div class="abs offer-shade"></div>
<div class="abs center script" style="top:2308px;color:#bbb">limited offer</div>
<h2 class="abs center offer-title" style="top:2370px">SIGN UP &amp; STAND TO WIN A ONE-NIGHT FREE STAY (WORTH RM250)</h2>
<p class="abs center" style="top:2416px;color:#eee;font-size:13px">We hate spam as you do, so your email is 100% safe with us.</p>
<div class="abs email">Enter your Email</div>
<div class="abs agree"><i></i>I agree to the T&amp;C View Contest T&amp;C</div>
<div class="abs btn-solid" style="left:421px;top:2552px;width:173px;height:46px">JOIN NOW</div>

<div class="abs partners"></div>
<div class="abs badge" style="left:176px;width:140px;background:#1f3f8a"></div>
<div class="abs badge" style="left:431px;width:100px;background:#e8505b"></div>
<div class="abs badge" style="left:612px;width:210px;background:#e0a24a"></div>
<div class="abs badge" style="left:862px;width:176px;background:#b5121b"></div>

<div class="abs footer"></div>
<h3 class="abs f-head" style="left:131px;font-weight:700">MAPLE RX VENTURES</h3>
<p class="abs f-text" style="left:131px;top:2928px;width:248px">Lorem ipsum dolor sit amet, dolor aliquam vehicula, eget vehicula condi-mentum ante arcu, sed amet imperdiet urna, dictum phasellus dolor. Parturient vel sed felis montes dui, rutrum nullam auctor orci ea id, sed amet massa nibh, hac eget ipsum suscipit eget hendrerit, sed ridiculus enim.</p>
<h3 class="abs f-head" style="left:446px;font-weight:500">CONTACT US</h3>
<div class="abs f-text" style="left:446px;top:2926px;width:280px">
  <div class="contact-row"><svg width="14" height="18" viewBox="0 0 24 28" style="margin-top:4px;flex:none"><path fill="#fff" d="M12 0a9 9 0 0 0-9 9c0 7 9 19 9 19s9-12 9-19a9 9 0 0 0-9-9zm0 13a4 4 0 1 1 0-8 4 4 0 0 1 0 8z"/></svg><span>L12-07 Cedar Court, Jalan Seroja, Taman Bayu, 81200 Johor Bahru.</span></div>
  <div class="contact-row" style="margin-top:18px"><svg width="14" height="14" viewBox="0 0 24 24" style="flex:none"><path fill="#fff" d="M6.6 10.8a15 15 0 0 0 6.6 6.6l2.2-2.2a1 1 0 0 1 1-.25 11 11 0 0 0 3.6.6 1 1 0 0 1 1 1V20a1 1 0 0 1-1 1A17 17 0 0 1 3 4a1 1 0 0 1 1-1h3.5a1 1 0 0 1 1 1 11 11 0 0 0 .6 3.6 1 1 0 0 1-.25 1z"/></svg><span>+65 8123 4567</span></div>
</div>
<h3 class="abs f-head" style="left:769px;font-weight:500">QUICK LINKS</h3>
<div class="abs f-links" style="left:769px;top:2922px">Home<br>Terms &amp; Conditions<br>FAQ<br>Newsletter</div>
<div class="abs f-links" style="left:940px;top:2922px">Let's Talk<br>Our Story<br>Blog<br>Our Services</div>
<div class="abs footer-base">Copyright © 2019 Maple Rx Ventures LLP</div>

</body>
</html>
```